Medical Waste Company with Logo

Need a business card design that targets office managers in the medical community. This card will be the front line for our sales team to market our services to the community. We would like to have email, phone number, website. Please use the logo attached to create a design that we would be proud of.

Target Market(s)

Medical Clients

Industry/Entity Type

Medical Supply

Contact Information for Business Card

Please use logo attached

Colors

Designer to choose colors to be used in the design.

Requirements
Must have
• Our logo (see attached file)
Nice to have
• Maybe a pop of some sort, raised..?

```html
<!DOCTYPE html>
<html lang="en">
<head>
<meta charset="utf-8">
<title>Northpeak Clinical Disposal – Business Card</title>
<link rel="stylesheet" href="https://fonts.googleapis.com/css2?family=Roboto:ital,wght@0,400;0,700;1,700&display=swap">
<style>
  :root {
    --page-bg: #1c1d20;
    --card-white: #f1f1f0;
    --brand-blue: #0f5f9a;
    --brand-blue-deep: #0b3f72;
    --brand-blue-light: #2377ad;
    --brand-gray: #6f7072;
    --text-dark: #2a2b2d;
    --rule: #b9babb;
  }
  * { box-sizing: border-box; margin: 0; padding: 0; }
  html, body {
    width: 1200px; height: 1053px; overflow: hidden;
    background: var(--page-bg);
    font-family: "Roboto", Arial, sans-serif;
  }
  .sheet {
    width: 1200px; height: 1053px;
    display: flex; flex-direction: column; align-items: center; justify-content: center;
    gap: 40px;
  }
  .card {
    position: relative;
    width: 800px; height: 457px;
    overflow: hidden;
    box-shadow: 0 10px 30px rgba(0,0,0,.5);
  }

  /* Front */
  .card--front { background: var(--card-white); }
  .contact { position: absolute; left: 54px; top: 72px; }
  .contact__name {
    font-weight: 700; font-style: italic; font-size: 34px; color: var(--brand-blue);
    letter-spacing: -.3px;
  }
  .contact__title { font-size: 19px; color: var(--text-dark); margin-top: 4px; }
  .divider {
    position: absolute; left: 54px; right: 54px; top: 168px;
    height: 1px; background: var(--rule);
  }
  .contact-list {
    position: absolute; left: 54px; top: 186px; list-style: none;
  }
  .contact-list li {
    display: flex; align-items: center; gap: 14px;
    font-size: 19px; color: var(--text-dark); line-height: 34px;
  }
  .contact-list svg { width: 18px; height: 18px; flex: none; }
  .wordmark {
    position: absolute; right: 54px; top: 72px;
    display: flex; align-items: center; gap: 12px;
    font-weight: 700; font-size: 26px; color: var(--brand-blue);
    letter-spacing: 1px; text-transform: uppercase;
  }
  .wordmark__mark { width: 22px; height: 22px; background: var(--brand-blue); flex: none; }
  .address {
    position: absolute; right: 54px; top: 290px;
    text-align: right; font-size: 19px; line-height: 28px; color: var(--text-dark);
  }
  .band { position: absolute; left: 0; bottom: 0; width: 800px; height: 40px; }

  /* Back */
  .card--back {
    background: radial-gradient(ellipse at 65% 30%, var(--brand-blue-light) 0%, var(--brand-blue) 45%, var(--brand-blue-deep) 100%);
    display: flex; align-items: center; justify-content: center;
  }
  .wordmark--back {
    position: static; color: #ffffff; font-size: 40px; gap: 18px; letter-spacing: 2px;
  }
  .wordmark--back .wordmark__mark { width: 32px; height: 32px; background: #ffffff; }
</style>
</head>
<body>
<main class="sheet">
  <section class="card card--front" aria-label="Business card front">
    <div class="contact">
      <h1 class="contact__name">Daniel Hart</h1>
      <p class="contact__title">Managing Director</p>
    </div>
    <div class="divider"></div>
    <ul class="contact-list">
      <li>
        <svg viewBox="0 0 24 24" aria-hidden="true"><path fill="#2a2b2d" d="M6.6 10.8a15 15 0 0 0 6.6 6.6l2.2-2.2a1 1 0 0 1 1-.25 11.4 11.4 0 0 0 3.6.57 1 1 0 0 1 1 1V20a1 1 0 0 1-1 1A17 17 0 0 1 3 4a1 1 0 0 1 1-1h3.5a1 1 0 0 1 1 1c0 1.25.2 2.45.57 3.57a1 1 0 0 1-.25 1z"/></svg>
        000 000 0000
      </li>
      <li>
        <svg viewBox="0 0 24 24" aria-hidden="true"><rect x="2.5" y="5" width="19" height="14" fill="none" stroke="#2a2b2d" stroke-width="1.6"/><path d="M2.5 5l9.5 8 9.5-8" fill="none" stroke="#2a2b2d" stroke-width="1.6"/></svg>
        daniel@northpeakclinical.com
      </li>
      <li>
        <svg viewBox="0 0 24 24" aria-hidden="true"><g fill="none" stroke="#2a2b2d" stroke-width="1.5"><circle cx="12" cy="12" r="9.5"/><ellipse cx="12" cy="12" rx="4.2" ry="9.5"/><path d="M2.5 12h19M4 7h16M4 17h16"/></g></svg>
        www.northpeakclinical.com
      </li>
    </ul>
    <div class="wordmark"><span class="wordmark__mark"></span>Northpeak Clinical</div>
    <address class="address" style="font-style:normal">
      450 Harbour Ave. Suite 210<br>Surrey<br>BC V3T2K8
    </address>
    <svg class="band" viewBox="0 0 800 40" preserveAspectRatio="none" aria-hidden="true">
      <rect x="0" y="14" width="800" height="26" fill="var(--brand-blue)"/>
      <polygon points="0,0 58,0 58,40 0,40" fill="var(--brand-gray)"/>
      <polygon points="58,0 80,0 80,40 58,40" fill="var(--brand-blue)"/>
    </svg>
  </section>

  <section class="card card--back" aria-label="Business card back">
    <div class="wordmark wordmark--back"><span class="wordmark__mark"></span>Northpeak Clinical</div>
  </section>
</main>
</body>
</html>
```